Investment Group needs a web page design

We need a web page design for a San Francisco-based investment group called 'Talvirow LLC'. The final design should be stylish and attractive to the idea while retaining a sense of stability and professionalism. A great example is http://brambleharborgroup.com/.

I am attaching the group's logo which should be the base for the webpage design.
Updates

Please note that I am interested in a single webpage that presents basic information. See the following example: http://brambleharborgroup.com/

Target Market(s)

persons doing initial due diligence and trying to assess what kind of group we are.

Industry/Entity Type

Investment

Font styles to use
Serif

Colors
86acd3
3176b5
0355a3

Requirements
Nice to have
• Would love the design to incorporate the concept - 'Sen no Sen: a block and counter attack while the opponent is attacking.'
Should not have
• Do not include trite illustrations related to finance, money or investing.

```html
<!DOCTYPE html>
<html lang="en">
<head>
<meta charset="utf-8">
<title>Talvirow</title>
<link rel="stylesheet" href="https://fonts.googleapis.com/css2?family=Josefin+Sans:wght@400;600;700&display=swap">
<style>
  :root {
    --ink: #111111;
    --white: #ffffff;
    --accent: #2a79bf;
    --navy: #0355a3;
    --navy-deep: #023f7c;
    --sky: #86acd3;
    --footer: #3176b5;
    --font: "Josefin Sans", sans-serif;
  }
  * { box-sizing: border-box; margin: 0; padding: 0; }
  html, body { width: 1200px; height: 990px; overflow: hidden; background: var(--white); }
  body { position: relative; font-family: var(--font); }

  .site-header { position: absolute; left: 0; top: 0; width: 1200px; height: 89px; background: var(--white); }
  .brand { position: absolute; left: 160px; top: 36px; display: flex; align-items: center; gap: 8px; }
  .brand-mark { width: 28px; height: 28px; background: var(--ink); }
  .brand-name { font-size: 31px; font-weight: 400; color: var(--ink); letter-spacing: 1px; line-height: 1; padding-top: 4px; }
  .main-nav { position: absolute; top: 47px; left: 0; width: 100%; }
  .main-nav a { position: absolute; font-size: 12px; font-weight: 600; color: var(--ink); text-decoration: none; white-space: nowrap; }
  .main-nav a.is-active { color: var(--accent); }
  .login-button { position: absolute; left: 965px; top: 41px; width: 74px; height: 25px; background: var(--navy); color: var(--white); font-size: 12.5px; font-weight: 600; display: flex; align-items: center; justify-content: center; padding-top: 3px; }

  .hero { position: absolute; left: 0; top: 89px; width: 1200px; height: 558px; }
  .hero-image { position: absolute; inset: 0; background: radial-gradient(ellipse at 50% 30%, #e4e4e4 0%, #9a9a9a 35%, #4a4a4a 70%, #151515 100%); }
  .hero-caption { position: absolute; left: 0; width: 100%; top: 488px; text-align: center; color: var(--white); font-size: 21px; font-weight: 400; }
  .hero-dots { position: absolute; top: 525px; left: 566px; display: flex; gap: 5px; }
  .hero-dots span { width: 13px; height: 13px; border-radius: 50%; background: var(--white); border: 1px solid #bbb; }
  .hero-dots span.is-current { background: var(--accent); border-color: var(--accent); }

  .welcome { position: absolute; left: 0; top: 647px; width: 1200px; height: 241px; background: linear-gradient(180deg, var(--navy-deep), var(--navy) 60%, #034c93); text-align: center; color: var(--white); }
  .welcome h1 { position: absolute; top: 38px; width: 100%; font-size: 15.5px; font-weight: 700; letter-spacing: 0.3px; }
  .welcome p { position: absolute; left: 190px; width: 820px; top: 74px; font-size: 13px; line-height: 22px; font-weight: 400; }
  .cta { position: absolute; left: 507px; top: 159px; width: 187px; height: 47px; background: var(--sky); color: var(--white); font-size: 15.5px; font-weight: 700; display: flex; align-items: center; justify-content: center; padding-top: 3px; }

  .site-footer { position: absolute; left: 0; top: 888px; width: 1200px; height: 102px; background: var(--footer); color: var(--white); }
  .footer-nav { position: absolute; left: 162px; top: 26px; display: flex; font-size: 14px; }
  .footer-nav a { color: var(--white); text-decoration: none; }
  .footer-nav .sep { margin: 0 18px; }
  .copyright { position: absolute; left: 162px; top: 57px; font-size: 14px; }
  .social { position: absolute; left: 953px; top: 38px; display: flex; gap: 7px; }
  .social span { width: 24px; height: 24px; border-radius: 50%; background: var(--white); }
</style>
</head>
<body>
  <header class="site-header">
    <div class="brand"><span class="brand-mark"></span><span class="brand-name">TALVIROW</span></div>
    <nav class="main-nav">
      <a class="is-active" style="left:435px">HOME</a>
      <a style="left:501px">ABOUT US</a>
      <a style="left:590px">INVESTMENTS</a>
      <a style="left:701px">SERVICES</a>
      <a style="left:786px">FAQ'S</a>
      <a style="left:850px">CONTACT US</a>
    </nav>
    <div class="login-button">LOGIN</div>
  </header>

  <section class="hero">
    <div class="hero-image" role="img" aria-label="Black and white photo looking up between tall office towers at a skyscraper"></div>
    <p class="hero-caption">Neque porro quisquam est qui dolorem ipsum quia dolor sit amet ...</p>
    <div class="hero-dots"><span class="is-current"></span><span></span><span></span><span></span></div>
  </section>

  <section class="welcome">
    <h1>WELCOME TO TALVIROW</h1>
    <p>Lorem Ipsum is simply dummy text of the printing and typesetting industry. Lorem Ipsum has been the industry's standard dummy text ever since the 1500s, when an unknown printer took a galley of type and scrambled it to make a type specimen book. It has survived not only five centuries, but also the leap into electronic typesetting, remaining essentially unchanged.</p>
    <div class="cta">Get Started To Invest</div>
  </section>

  <footer class="site-footer">
    <nav class="footer-nav">
      <a>Home</a><span class="sep">|</span>
      <a>About Us</a><span class="sep">|</span>
      <a>Investments</a><span class="sep">|</span>
      <a>Services</a><span class="sep">|</span>
      <a>FAQ's</a><span class="sep">|</span>
      <a>Contact Us</a>
    </nav>
    <p class="copyright">© 2014 Company Name ,All Rights reserved</p>
    <div class="social" aria-label="Social links"><span></span><span></span><span></span></div>
  </footer>
</body>
</html>
```